Mailer Postcard for Potential Bankruptcy Clients

The postcard will be printed at 8.5"x6" to abide by the specification at the following link: https://www.mailvortex.example/art-upload/guide/. I want an attractive two sided post card that includes my logo (see attachment). The design would have to have room for the website address, phone number, two location addresses and give them information about a civil action pending against them (You are being sued in X county (case# xxyx). We can help.). I don't really like the visuals of the attached postcard, so please use as a general guide for what I am trying to do. Ultimately, I want an ad that gets people to call me so I can help them.

I also want it to be compatible with the website (CreditHarbor.Legal).

Target Market(s)

Potential bankruptcy clients.

Industry/Entity Type

Legal

Colors

Designer to choose colors to be used in the design.

Requirements
Must have
• Phone number, addresses, website, and place for text regarding pending legal action against the receiver. Should say something to the effect: You have a pending legal action in (county name) County (court name [superior, magistrate, ect.]). Let us help you deal with it responsibly.
• Please note the design specifications at this link:

```html
<!DOCTYPE html>
<html lang="en">
<head>
<meta charset="utf-8">
<title>Credit Harbor Law Group – Mailer Postcard</title>
<link rel="stylesheet" href="https://fonts.googleapis.com/css2?family=Lato:ital,wght@0,400;0,700;1,400;1,700&family=Oswald:wght@500;600&family=Roboto+Condensed:wght@700&display=swap">
<style>
:root{
  --green:#5f9a6a;
  --green-light:#8cc49a;
  --ink:#1a1a1a;
  --band:#111;
  --grey:#6d6d6d;
  --paper:#fff;
  --page:#fff;
  --stamp:#8f8f8f;
}
*{box-sizing:border-box;margin:0;padding:0}
html,body{width:900px;height:1200px;overflow:hidden;background:var(--page)}
body{position:relative;font-family:'Lato',sans-serif;color:var(--ink)}
.card{position:absolute;left:70px;width:760px;height:493px;background:var(--paper);box-shadow:0 2px 6px rgba(0,0,0,.35);overflow:hidden}
.card--front{top:42px;background:linear-gradient(90deg,#fff 0%,#fafafa 55%,#eeeeee 100%)}
.card--back{top:628px}
.side-label{position:absolute;left:0;width:900px;text-align:center;font:italic 400 34px 'Lato',sans-serif;color:#222}
.abs{position:absolute}
.photo{position:absolute}
.brand{position:absolute;display:flex;align-items:center;gap:10px}
.brand__dot{flex:none;width:22px;height:22px;border-radius:50%;background:var(--green)}
.brand__name{font:400 29px/1.05 'Lato',sans-serif;color:#3a3a3a}
.brand__sub{position:absolute;font:italic 400 11px 'Lato',sans-serif;color:var(--green);white-space:nowrap}
.divider{position:absolute;width:2px;background:#b9b9b9}
.call-label{font:700 17px 'Roboto Condensed',sans-serif;color:#111;letter-spacing:.2px;white-space:nowrap}
.phone{font:600 37px 'Oswald',sans-serif;color:var(--green);line-height:1.05;white-space:nowrap}
.hero{position:absolute;left:0;top:155px;width:760px;height:180px;background:linear-gradient(90deg,#000 0%,#1e1e1e 55%,#3a3a3a 100%)}
.hero__title{position:absolute;left:210px;top:26px;font:500 27px 'Oswald',sans-serif;color:#fff;letter-spacing:.3px;white-space:nowrap}
.hero__title em{font-style:normal;color:var(--green-light)}
.hero__copy{position:absolute;left:210px;top:68px;width:537px;font:italic 400 11.4px/14.4px 'Lato',sans-serif;color:#fff;text-align:justify}
.notice{position:absolute;left:27px;top:382px;width:305px;font:italic 700 12.6px/16px 'Lato',sans-serif;color:#111;text-align:justify}
.map{position:absolute;left:363px;top:358px;width:113px;height:120px;border:3px solid #3d6b47;background:linear-gradient(135deg,#eceee6,#dfe3d8)}
.addr-title{position:absolute;left:495px;top:362px;font:600 22px 'Oswald',sans-serif;color:var(--green);display:flex;align-items:center;gap:8px}
.addr-title::after{content:"";width:155px;height:2px;background:#111}
.addr{position:absolute;left:495px;width:252px;font:italic 700 12px/15px 'Lato',sans-serif;color:#111;padding-left:16px}
.addr::before{content:"";position:absolute;left:0;top:4px;width:7px;height:7px;border-radius:50%;background:var(--green)}
.visit{position:absolute;left:27px;top:465px;font:italic 700 13px 'Lato',sans-serif;color:#111;letter-spacing:.5px}
.visit span{letter-spacing:3.2px}
.services-head{position:absolute;left:148px;top:157px;width:128px;height:30px;background:#0d0d0d;border:2px solid #fff;outline:2px solid var(--green);color:var(--green-light);font:600 19px/26px 'Oswald',sans-serif;text-align:center}
.svc{position:absolute}
.svc--left{left:16px;width:180px}
.svc--right{left:216px;width:210px}
.svc__title{font:700 12.6px 'Roboto Condensed',sans-serif;color:var(--green);display:flex;align-items:center;gap:3px;white-space:nowrap}
.svc__title i{display:inline-block;width:7px;height:8px;background:var(--green);border-radius:0 0 4px 4px}
.svc__body{margin-left:10px;font:400 10.2px/13.4px 'Lato',sans-serif;color:#111;text-align:justify}
.visit-small{position:absolute;left:19px;top:475px;font:400 11px 'Lato',sans-serif;color:#fff}
.visit-small span{letter-spacing:3px}
.stamp{position:absolute;left:668px;top:159px;width:65px;height:81px;background:var(--stamp)}
.mail-line{position:absolute;left:500px;width:235px;height:1px;background:#8a8a8a}
</style>
</head>
<body>

<!-- FRONT -->
<section class="card card--front">
  <div class="photo" role="img" aria-label="Smiling attorney in dark suit holding a folder" style="left:0;top:28px;width:180px;height:310px;background:linear-gradient(180deg,#d9d4cf 0%,#2a3142 40%,#1d2230 100%)"></div>

  <div class="brand" style="left:190px;top:46px">
    <span class="brand__dot"></span>
    <span class="brand__name">Credit Harbor<br>Law Group</span>
  </div>
  <p class="brand__sub" style="left:250px;top:111px">by Attorney M. Castellan</p>

  <div class="divider" style="left:463px;top:33px;height:95px"></div>
  <div class="abs" style="left:495px;top:50px">
    <p class="call-label">CALL US FOR MORE INFORMATION</p>
    <p class="phone">(404) 555-0187</p>
  </div>

  <svg class="abs" style="left:0;top:135px" width="760" height="210" viewBox="0 0 760 210">
    <polygon points="0,6 620,14 760,0 760,20 0,20" fill="#5f9a6a"/>
    <polygon points="0,196 760,196 760,208 0,208" fill="#5f9a6a"/>
  </svg>
  <div class="hero">
    <h1 class="hero__title"><em>GET OUT OF DEBT AND</em> RESTORE YOUR CREDIT</h1>
    <p class="hero__copy">We are a Georgia Law Firm that is dedicated to being a one-stop shop for all debt woes that Georgians face. We are experienced bankruptcy attorneys that understand that people need more than just a bankruptcy lawyer. People need someone that is experienced in handling all of the practical aspects of avoiding bankruptcy, recovering from bankruptcy quickly, tackling stubborn student loans, and punishing abusive debt collectors when they violate the law. If you came to this website and have read this far, you should contact us to see if we can help you.</p>
  </div>
  <div class="photo" role="img" aria-label="Attorney portrait continued over the dark band" style="left:0;top:155px;width:180px;height:180px;background:linear-gradient(180deg,#1d2230,#121620)"></div>
  <svg class="abs" style="left:0;top:333px" width="760" height="16" viewBox="0 0 760 16">
    <polygon points="170,0 760,0 760,14 300,8" fill="#5f9a6a"/>
  </svg>

  <p class="notice">You have a pending legal action in (county name) County (court name [superior, magistrate, ect.]). Let us help you deal with it responsibly.</p>

  <div class="map" role="img" aria-label="Street map of Atlanta with two office location pins"></div>

  <h2 class="addr-title">ADDRESS</h2>
  <p class="addr" style="top:400px">418 Magnolia Row, NW Suite #1400 Atlanta, Georgia 30303</p>
  <p class="addr" style="top:446px">5120 Cedar Bend Rd. Douglasville, Georgia 30134</p>

  <svg class="abs" style="left:0;top:456px" width="760" height="37" viewBox="0 0 760 37">
    <polygon points="0,4 318,4 340,29 0,29" fill="#111"/>
    <polygon points="0,6 312,6 330,27 0,27" fill="#7db78b"/>
    <rect x="0" y="29" width="760" height="8" fill="#111"/>
  </svg>
  <p class="visit">VISIT US - <span>creditharbor.legal</span></p>
</section>
<p class="side-label" style="top:548px">front</p>

<!-- BACK -->
<section class="card card--back">
  <div class="photo" role="img" aria-label="Advisor meeting a smiling couple reviewing paperwork at a desk" style="left:0;top:0;width:242px;height:164px;background:linear-gradient(135deg,#e9ecef 0%,#c9c2b8 55%,#2a2f3a 100%)"></div>
  <div class="photo" role="img" aria-label="Two lawyers reviewing documents in a law library" style="left:250px;top:0;width:200px;height:164px;background:linear-gradient(135deg,#6b4f36 0%,#3d3028 50%,#20242c 100%)"></div>

  <svg class="abs" style="left:0;top:0" width="760" height="493" viewBox="0 0 760 493">
    <rect x="450" y="0" width="8" height="493" fill="#111"/>
    <polygon points="458,0 475,0 475,22 458,22" fill="#5f9a6a"/>
    <rect x="18" y="170" width="407" height="2" fill="#111"/>
    <rect x="458" y="0" width="3" height="493" fill="#5f9a6a"/>
  </svg>
  <div class="services-head">OUR SERVICES</div>

  <div class="svc svc--left" style="top:198px">
    <p class="svc__title"><i></i>Mortgage Loan Modifications</p>
    <p class="svc__body">We help people reduce their mortgage payments and change their terms to suit their current ability to pay and stay in their homes.</p>
  </div>
  <div class="svc svc--left" style="top:283px">
    <p class="svc__title"><i></i>Student Loans</p>
    <p class="svc__body">We help former students with the discharge of certain student loans and in navigating their repayment options.</p>
  </div>
  <div class="svc svc--left" style="top:354px">
    <p class="svc__title"><i></i>Bankruptcy</p>
    <p class="svc__body" style="font-style:italic">We file both Chapter 7 (Liquidation) and Chapter 13 (wage-earners repayment plans) for our clients depending on their individual situation. Bankruptcy is a powerful tool to stop creditors in their tracks immediately.</p>
  </div>
  <div class="svc svc--right" style="top:198px">
    <p class="svc__title"><i></i>Credit Report Inaccuracies &amp; Errors</p>
    <p class="svc__body">We prosecute creditors for violations of the Fair Credit Reporting Act (FCRA) on behalf of our clients to recovery damages (possibly even punitive damages) and attorneys' fees.</p>
  </div>
  <div class="svc svc--right" style="top:283px">
    <p class="svc__title"><i></i>Debt Collection Violations</p>
    <p class="svc__body">We prosecute violations of The Fair Debt Collection Practices Act (FDCPA), which protects people from harassment by debt collectors and make them pay your attorneys' fees and get compensation as well.</p>
  </div>
  <div class="svc svc--right" style="top:382px">
    <p class="svc__title"><i></i>Free Credit Rebuilding Program</p>
    <p class="svc__body">We have contracted with www.steadyscorepath.com to provide their 7 Steps to a Steady Score Path (typically $1,000 on its own), for free to our past and present clients.</p>
  </div>

  <svg class="abs" style="left:0;top:462px" width="460" height="31" viewBox="0 0 460 31">
    <polygon points="0,0 205,0 232,31 0,31" fill="#111"/>
    <polygon points="212,16 450,16 450,31 226,31" fill="#7db78b"/>
  </svg>
  <p class="visit-small">visit us - <span>creditharbor.legal</span></p>

  <div class="brand" style="left:540px;top:20px;gap:8px">
    <span class="brand__dot" style="width:15px;height:15px"></span>
    <span class="brand__name" style="font-size:19px">Credit Harbor<br>Law Group</span>
  </div>
  <p class="brand__sub" style="left:585px;top:63px;font-size:8px">by Attorney M. Castellan</p>

  <div class="stamp"></div>
  <div class="mail-line" style="top:314px"></div>
  <div class="mail-line" style="top:347px"></div>
  <div class="mail-line" style="top:382px"></div>
</section>
<p class="side-label" style="top:1130px">back</p>

</body>
</html>
```